Meridel Advisory & Coaching Collective Web Site Design

Help!

We have started designing and building a Web site to promote and sell training services to HR managers. But we are not very good designers. In fact, we stink.

We have a logo.

We have most of the content (more or less) and the site architecture. But we have put together a pretty lousy look and feel.

Take a look: http://brightlowpath.example/vortalindex.html

What we'd like is a Web 3.0 type design - clean, simple, modern looking. Some sites we admire:

pinvale.example
trelosk.example
skivorn.example
quibbledot.example
morpa.example

We have access to stock photography, some of which we've used on the site we've built so far. You can use those and others. But keep it simple.

Target Market(s)

Professional HR managers in larger companies

Requirements
Must have
• Use our logo and a color scheme based off of it. Logo file uploaded.

Need to see home page and examples of secondary pages, based on site currently online.

```html
<!DOCTYPE html>
<html lang="en">
<head>
<meta charset="utf-8">
<title>Brightlow Path for Corvane HR</title>
<link rel="stylesheet" href="https://fonts.googleapis.com/css2?family=Ubuntu:wght@500;700&family=Arimo:wght@400;700&display=swap">
<style>
:root{
  --top-rule:#8ea2c9;
  --brand-blue:#0e3ea8;
  --nav-top:#2a5fcf;
  --nav-bottom:#0f3a9e;
  --sky:#3cb9e8;
  --head-dark:#1a3f9c;
  --text:#222;
  --muted:#8a8a8a;
  --band:#f1f1f1;
  --line:#cfcfcf;
  --red:#d23b3b;
  --red-dark:#a01f22;
  --orange:#f6951f;
  --orange-dark:#d46d08;
  --green:#5fca5f;
  --green-dark:#1c8d2c;
  --navy:#0c2f8a;
}
*{margin:0;padding:0;box-sizing:border-box}
html,body{width:1200px;height:788px;overflow:hidden;background:#fff}
body{position:relative;font-family:Arimo,Arial,sans-serif;color:var(--text)}
.page{position:absolute;inset:0;overflow:hidden}
.masthead{position:absolute;left:0;top:0;width:1200px;height:158px;border-top:4px solid var(--top-rule);background:linear-gradient(#fff,#f2f2f2)}
.sky{position:absolute;left:0;top:158px;width:1200px;height:445px;background:linear-gradient(var(--sky) 0%,#8ed6f3 45%,#fff 80%);z-index:0}
.brand{position:absolute;left:116px;top:52px;display:flex;align-items:center;gap:10px;font-family:Arimo,Arial,sans-serif;font-size:32px;font-weight:700;color:var(--brand-blue)}
.brand-dot{width:30px;height:30px;border-radius:50%;background:var(--brand-blue)}
.phone{position:absolute;right:117px;top:54px;display:flex;align-items:center;gap:6px;font-family:Arimo,Arial,sans-serif;font-weight:700;font-size:17px;color:var(--brand-blue)}
.main-nav{position:absolute;left:118px;top:136px;z-index:5}
.nav{width:966px;height:38px;border-radius:3px;background:linear-gradient(var(--nav-top),var(--nav-bottom));display:flex;list-style:none;box-shadow:0 1px 2px rgba(0,0,0,.25)}
.nav li{display:flex;align-items:center;justify-content:center;height:38px;color:#fff;font-size:12px;font-weight:700;border-right:1px solid #0a2f86;box-shadow:1px 0 0 #3f73da}
.nav li:last-child{border-right:0;box-shadow:none}
.headline{position:absolute;left:0;top:198px;width:1200px;text-align:center;font-family:Ubuntu,sans-serif;font-weight:700;font-size:34px;color:var(--head-dark);z-index:1}
.headline .lead{color:#fff}
.card{position:absolute;top:266px;width:293px;height:299px;background:#fff;border-radius:4px;box-shadow:0 1px 4px rgba(0,0,0,.15);z-index:1}
.card .photo{position:absolute;left:6px;top:8px;width:280px;height:233px;border-radius:3px}
.card .ribbon{position:absolute;left:-8px;top:174px;width:309px;height:54px}
.card .ribbon span{position:absolute;left:0;right:0;top:14px;text-align:center;color:#fff;font-family:Arimo,Arial,sans-serif;font-weight:700;font-size:23px;text-shadow:0 1px 1px rgba(0,0,0,.35)}
.card p{position:absolute;left:0;right:0;top:251px;text-align:center;font-size:14px;line-height:17px}
.card-gen101{left:126px;border-bottom:3px solid #e06464}
.card-gaps{left:456px;border-bottom:3px solid #f7b05a}
.card-strategies{left:785px;border-bottom:3px solid #7ed37e}
.photo-meeting{background:linear-gradient(135deg,#3a2e28,#8a7c70 55%,#4b4038)}
.photo-gaps{background:linear-gradient(135deg,#c9c9c9,#f4f4f4 45%,#6b6b6b)}
.photo-team{background:linear-gradient(135deg,#e9ecef,#c8b8a4 50%,#3c3f48)}
.band{position:absolute;left:0;top:603px;width:1200px;height:121px;background:var(--band)}
.band-line{position:absolute;left:117px;width:968px;height:1px;background:var(--line)}
.tile{position:absolute;top:626px;width:235px;height:78px;border-radius:3px;display:flex;align-items:center;color:#fff;font-weight:700;font-size:25px}
.tile svg,.tile .icon{position:absolute}
.tile .label{position:absolute;top:23px}
.tile-resources{left:116px;background:var(--red);box-shadow:inset 0 -3px 0 var(--red-dark)}
.tile-training{left:362px;background:var(--green);box-shadow:inset 0 -3px 0 #3fa43f}
.tile-tools{left:606px;background:var(--orange);box-shadow:inset 0 -3px 0 var(--orange-dark)}
.tile-discuss{left:851px;background:var(--navy);box-shadow:inset 0 -3px 0 #06215f}
.footer-links{position:absolute;left:122px;top:747px;display:flex;list-style:none;font-size:11px;color:var(--muted)}
.footer-links .current{color:#222;font-weight:700}
.legal{position:absolute;right:114px;top:748px;font-size:11px;color:var(--muted)}
.legal b{color:#777}
</style>
</head>
<body>
<div class="page">
  <header class="masthead">
    <div class="brand"><span class="brand-dot"></span>Brightlow Path for Corvane HR</div>
    <div class="phone">
      <svg width="56" height="36" viewBox="0 0 56 36"><path d="M4 12c0-7 48-7 48 0v4h-10v-4c-6-2-22-2-28 0v4H4z" fill="#222"/><path d="M12 16h32l6 18H6z" fill="#333"/><circle cx="28" cy="25" r="6" fill="#777"/></svg>
      CALL US 555 0142-700
    </div>
  </header>

  <div class="sky"></div>

  <nav class="main-nav">
    <ul class="nav">
      <li style="width:54px"><svg width="20" height="18" viewBox="0 0 20 18"><path d="M10 1L1 9h3v8h4v-5h4v5h4V9h3z" fill="#fff"/></svg></li>
      <li style="width:93px">ABOUT US</li>
      <li style="width:101px">GEN 101</li>
      <li style="width:100px">GEN GAPS</li>
      <li style="width:107px">STRATEGIES</li>
      <li style="width:111px">RESOURCES</li>
      <li style="width:98px">TRAINING</li>
      <li style="width:83px">TOOLS</li>
      <li style="width:91px">DISCUSS</li>
      <li style="width:128px">CONTACT US</li>
    </ul>
  </nav>

  <h1 class="headline"><span class="lead">Generational Tools</span> and Training for HR Professionals</h1>

  <section class="card card-gen101">
    <div class="photo photo-meeting" role="img" aria-label="Photo: overhead view of colleagues meeting around a table"></div>
    <div class="ribbon"><svg width="309" height="54" viewBox="0 0 309 54"><path d="M0 4h10v46H0z" fill="#7a1216"/><path d="M299 4h10v46h-10z" fill="#7a1216"/><rect x="4" y="8" width="301" height="38" fill="#d8343a"/><rect x="4" y="8" width="301" height="16" fill="#e8626a"/></svg><span>GENERATIONS 101</span></div>
    <p>Learn who the Generations are and<br>why they matter</p>
  </section>

  <section class="card card-gaps">
    <div class="photo photo-gaps" role="img" aria-label="Photo: senior executive listening in a business conversation"></div>
    <div class="ribbon"><svg width="309" height="54" viewBox="0 0 309 54"><path d="M0 4h10v46H0z" fill="#7a1216"/><path d="M299 4h10v46h-10z" fill="#7a1216"/><rect x="4" y="8" width="301" height="38" fill="#f08a12"/><rect x="4" y="8" width="301" height="16" fill="#f9b13c"/></svg><span>GENERATION GAPS</span></div>
    <p>Master the challenges created by<br>today's generational gaps</p>
  </section>

  <section class="card card-strategies">
    <div class="photo photo-team" role="img" aria-label="Photo: young team holding puzzle pieces"></div>
    <div class="ribbon"><svg width="309" height="54" viewBox="0 0 309 54"><path d="M0 4h10v46H0z" fill="#0d5a1a"/><path d="M299 4h10v46h-10z" fill="#0d5a1a"/><rect x="4" y="8" width="301" height="38" fill="#1d9a30"/><rect x="4" y="8" width="301" height="16" fill="#3dba4c"/></svg><span>GEN STRATEGIES</span></div>
    <p>Develop Successful Strategies that<br>drive your organization</p>
  </section>

  <div class="band"></div>
  <div class="band-line" style="top:603px"></div>
  <div class="band-line" style="top:724px"></div>

  <a class="tile tile-resources">
    <div class="icon" role="img" aria-label="Illustration: stack of books" style="left:16px;top:12px;width:56px;height:54px;border-radius:3px;background:linear-gradient(#9a9a9a,#4c4c4c)"></div>
    <span class="label" style="left:92px">Resources</span>
  </a>
  <a class="tile tile-training">
    <div class="icon" role="img" aria-label="Illustration: chalkboard on an easel" style="left:20px;top:6px;width:64px;height:64px;border-radius:3px;background:linear-gradient(#2f6b2a,#8a5a24)"></div>
    <span class="label" style="left:106px">Training</span>
  </a>
  <a class="tile tile-tools">
    <svg style="left:30px;top:10px" width="56" height="56" viewBox="0 0 56 56"><path d="M8 44L36 16" stroke="#222" stroke-width="8" stroke-linecap="round"/><circle cx="40" cy="12" r="10" fill="#222"/><circle cx="44" cy="8" r="5" fill="#f6951f"/><path d="M12 10l34 34" stroke="#222" stroke-width="6" stroke-linecap="round"/><path d="M8 6l8 8" stroke="#222" stroke-width="10" stroke-linecap="round"/></svg>
    <span class="label" style="left:122px">Tools</span>
  </a>
  <a class="tile tile-discuss">
    <svg style="left:18px;top:10px" width="84" height="54" viewBox="0 0 84 54"><ellipse cx="30" cy="22" rx="28" ry="20" fill="#4bb8ef"/><path d="M14 36l-6 12 16-8z" fill="#4bb8ef"/><ellipse cx="56" cy="30" rx="24" ry="18" fill="#f7a634"/><path d="M68 42l8 10-16-6z" fill="#f7a634"/></svg>
    <span class="label" style="left:112px">Discuss</span>
  </a>

  <footer>
    <ul class="footer-links">
      <li class="current" style="width:71px">Home</li>
      <li style="width:82px">About us</li>
      <li style="width:84px">GeN 101</li>
      <li style="width:90px">Gen Gaps</li>
      <li style="width:89px">Strategies</li>
      <li style="width:108px">Privacy Policy</li>
      <li>Contact us</li>
    </ul>
    <div class="legal">All Right Reserved, <b>Brightlow Path for Corvane HR</b></div>
  </footer>
</div>
</body>
</html>
```